New Web Design Project for kitchen company

We need a homepage mockup for a company that sells and installs kitchen and baths. Use your creative talent to come up with something visually appeal and professional for this web-site.

Please see the attached brief.

If you have any questions feel free to post them right on the project discussion.

Target Market(s)

homeowners

Number of Pages Required

1 page

Font styles to use
Serif
Other font styles liked:
• Something similar to the logo

```html
<!DOCTYPE html>
<html lang="en">
<head>
<meta charset="utf-8">
<title>Harborline Kitchen and Bath</title>
<link href="https://fonts.googleapis.com/css2?family=Marcellus&family=Lato:wght@400;700&display=swap" rel="stylesheet">
<style>
:root{
  --ink:#111111;
  --paper:#ffffff;
  --mist:#f2f2f2;
  --line:#9a9a9a;
  --muted:#555555;
  --faint:#c9c9c9;
  --wood-dark:#3a2a1e;
  --wood-mid:#7a5a3e;
  --steel:#8f8f8f;
  --footer:#1c1c1c;
  --footer-bar:#2a2a2a;
}
*{box-sizing:border-box;margin:0;padding:0}
html,body{width:1200px;height:4532px;overflow:hidden;background:var(--paper)}
body{position:relative;font-family:'Lato',sans-serif;color:var(--ink)}
.abs{position:absolute}
.serif{font-family:'Marcellus',serif;text-transform:uppercase}
.btn{position:absolute;display:flex;align-items:center;justify-content:center;border-radius:20px;font-family:'Lato',sans-serif;font-size:13px;font-weight:700}
.btn-dark{background:var(--ink);color:var(--paper)}
.btn-light{background:var(--paper);color:var(--ink);font-weight:400}
.section-title{position:absolute;left:0;width:1200px;text-align:center;font-family:'Marcellus',serif;font-size:29px;text-transform:uppercase}
.rule{position:absolute;height:2px;width:52px;background:var(--ink)}

/* header */
.brand{position:absolute;display:flex;align-items:center;gap:10px}
.brand-mark{width:46px;height:46px;border-radius:50%;border:2px solid currentColor}
.brand-name{font-family:'Marcellus',serif;font-size:21px;line-height:1;text-transform:uppercase}
.brand-name small{display:block;font-size:9px;letter-spacing:.5px;margin-top:3px}
.nav{position:absolute;top:48px;left:436px;display:flex;gap:30px;font-size:13px;color:var(--ink)}

/* hero */
.hero-photo{position:absolute;left:0;top:0;width:1200px;height:820px;
  background:linear-gradient(180deg,#d9d6d0 0%,#b6ada3 35%,#6e5747 62%,var(--wood-dark) 100%)}
.hero-ring{position:absolute;left:333px;top:124px;width:530px;height:530px;border-radius:50%;
  border:2px solid rgba(255,255,255,.85);background:rgba(20,20,20,.45)}
.hero-kicker{position:absolute;top:340px;left:0;width:1200px;text-align:center;color:var(--paper);font-family:'Marcellus',serif;font-size:19px;text-transform:uppercase}
.hero-title{position:absolute;top:366px;left:0;width:1200px;text-align:center;color:var(--paper);font-family:'Marcellus',serif;font-size:38px;text-transform:uppercase}

/* services */
.service{position:absolute;top:980px;width:300px;text-align:center}
.service-badge{width:206px;height:206px;margin:0 auto;border-radius:50%;border:2px solid var(--ink);display:flex;align-items:center;justify-content:center}
.service-badge .core{width:190px;height:190px;border-radius:50%;background:var(--ink);display:flex;align-items:center;justify-content:center}
.service h3{font-family:'Marcellus',serif;font-weight:400;font-size:15px;text-transform:uppercase;margin-top:28px}
.service p{font-size:12.5px;line-height:17px;color:var(--ink);margin-top:10px}

/* about */
.about-text{position:absolute;left:148px;top:1705px;width:445px;font-size:12px;line-height:18px;color:var(--muted)}
.about-photo{position:absolute;left:627px;top:1509px;width:422px;height:422px;border-radius:50%;border:3px solid var(--ink);padding:8px;background:var(--mist)}
.about-photo .fill{width:100%;height:100%;border-radius:50%;background:radial-gradient(circle at 50% 45%,#4f6b7a 0%,#8fa0aa 40%,#c9c3b8 70%,#7d5e45 100%)}

/* projects */
.project{position:absolute;top:2188px;width:300px;height:256px}

/* cta */
.cta-photo{position:absolute;left:0;top:2610px;width:1200px;height:426px;background:linear-gradient(180deg,#4c4238 0%,#6d6254 45%,#8a7e6c 75%,#3f362d 100%)}
.cta-photo::after{content:"";position:absolute;inset:0;background:rgba(0,0,0,.35)}

/* testimonials */
.quote-card{position:absolute;left:319px;top:3251px;width:549px;height:190px;border:2px solid var(--ink);background:var(--paper);box-shadow:0 4px 8px rgba(0,0,0,.25);text-align:center;padding:34px 46px 0}
.quote-card p{font-size:12.5px;line-height:22px}
.quote-card .who{font-family:'Marcellus',serif;font-size:15px;text-transform:uppercase;margin-top:20px}
.quote-side{position:absolute;top:3290px;width:240px;font-size:12.5px;line-height:22px;color:var(--faint);font-style:italic}
.qmark{position:absolute;font-family:'Marcellus',serif;font-size:34px;line-height:1}
.arrow{position:absolute;width:34px;height:34px;border-radius:50%;border:1.5px solid var(--ink);background:var(--paper);display:flex;align-items:center;justify-content:center}

/* contact */
.contact-bg{position:absolute;left:0;top:3700px;width:1200px;height:400px;background:linear-gradient(180deg,#ffffff 0%,#ebe7e2 35%,#d8d2ca 100%)}
.field{position:absolute;border:1px solid var(--ink);border-radius:18px;background:rgba(255,255,255,.55);font-size:12px;color:var(--muted);padding:9px 0 0 28px}

/* footer */
.footer{position:absolute;left:0;top:4080px;width:1200px;height:452px;background:var(--footer);color:var(--paper)}
.foot-head{position:absolute;top:4196px;font-family:'Marcellus',serif;font-size:20px;text-transform:uppercase;color:var(--paper)}
.foot-text{position:absolute;font-size:12.5px;line-height:18px;color:var(--paper)}
.foot-links{list-style:none}
.contact-row{position:absolute;left:632px;display:flex;gap:14px;font-size:12.5px;line-height:18px;color:var(--paper)}
.bottom-bar{position:absolute;left:0;top:4480px;width:1200px;height:52px;background:var(--footer-bar)}
.social{position:absolute;top:4496px;width:22px;height:22px;border-radius:50%;border:1.5px solid var(--paper)}
</style>
</head>
<body>

<!-- HERO -->
<div class="hero-photo" role="img" aria-label="Photo of a bright remodeled kitchen with white cabinets, a dark island and wood floors"></div>
<div class="brand" style="left:75px;top:32px;color:var(--ink)">
  <span class="brand-mark"></span>
  <span class="brand-name">Harborline<small>Kitchen and Bath, Inc</small></span>
</div>
<nav class="nav"><span>Home</span><span>About us</span><span>Services</span><span>Projects</span><span>Testimonials</span><span>Contact us</span></nav>
<div class="btn btn-dark" style="left:954px;top:39px;width:172px;height:36px;font-weight:400">Schedule A Consultation</div>

<div class="hero-ring"></div>
<div class="hero-kicker">Welcome to Harborline Kitchen and Bath</div>
<div class="hero-title">Committed to Quality</div>
<div class="btn btn-light" style="left:530px;top:449px;width:138px;height:33px">Explore our work</div>

<svg class="abs" style="left:0;top:755px" width="1200" height="70" viewBox="0 0 1200 70">
  <path d="M0 60 Q600 -10 1200 60 L1200 70 L0 70 Z" fill="#ffffff"/>
  <path d="M0 60 Q600 -10 1200 60 L1200 50 Q600 -28 0 50 Z" fill="#111111"/>
</svg>

<!-- SERVICES -->
<h2 class="section-title" style="top:872px">Our Services</h2>
<div class="rule" style="left:564px;top:912px"></div>

<div class="service" style="left:132px">
  <div class="service-badge"><div class="core">
    <svg width="80" height="80" viewBox="0 0 80 80" fill="none" stroke="#fff" stroke-width="5">
      <path d="M12 10 L12 70 L70 70 Z" stroke-linejoin="round"/>
      <path d="M24 40 L24 58 L42 58 Z" stroke-width="4"/>
      <path d="M34 14 L66 46 L60 52 L28 20 Z" fill="#fff" stroke="none"/>
    </svg>
  </div></div>
  <h3>Kitchen &amp; Bathroom Design</h3>
  <p>Lorem Ipsum is simply dummy text of the<br>printing and typesetting industry.</p>
</div>
<div class="btn btn-dark" style="left:229px;top:1313px;width:111px;height:35px">Read More</div>

<div class="service" style="left:445px">
  <div class="service-badge"><div class="core">
    <svg width="80" height="80" viewBox="0 0 80 80" fill="#fff">
      <rect x="36" y="4" width="9" height="72" rx="3" transform="rotate(45 40 40)"/>
      <rect x="36" y="4" width="9" height="72" rx="3" transform="rotate(-45 40 40)"/>
      <circle cx="16" cy="16" r="11"/>
      <rect x="58" y="8" width="14" height="10" transform="rotate(45 65 13)"/>
    </svg>
  </div></div>
  <h3>Kitchen &amp; Bathroom Remodeling</h3>
  <p>Lorem Ipsum is simply dummy text of the<br>printing and typesetting industry.</p>
</div>
<div class="btn btn-dark" style="left:543px;top:1313px;width:111px;height:35px">Read More</div>

<div class="service" style="left:756px">
  <div class="service-badge"><div class="core">
    <svg width="84" height="84" viewBox="0 0 84 84" fill="#fff">
      <g transform="translate(42 42)">
        <rect x="-6" y="-36" width="12" height="14"/><rect x="-6" y="22" width="12" height="14"/>
        <rect x="-36" y="-6" width="14" height="12"/><rect x="22" y="-6" width="14" height="12"/>
        <rect x="-6" y="-36" width="12" height="14" transform="rotate(45)"/><rect x="-6" y="22" width="12" height="14" transform="rotate(45)"/>
        <rect x="-36" y="-6" width="14" height="12" transform="rotate(45)"/><rect x="22" y="-6" width="14" height="12" transform="rotate(45)"/>
        <circle r="26"/>
        <circle r="13" fill="#111"/>
        <rect x="-4" y="0" width="8" height="44" rx="3" transform="rotate(-45)"/>
      </g>
    </svg>
  </div></div>
  <h3>Sales &amp; Installation</h3>
  <p>Lorem Ipsum is simply dummy text of the<br>printing and typesetting industry.</p>
</div>
<div class="btn btn-dark" style="left:853px;top:1313px;width:111px;height:35px">Read More</div>

<!-- ABOUT -->
<svg class="abs" style="left:0;top:1438px" width="1200" height="570" viewBox="0 0 1200 570">
  <path d="M0 0 Q600 40 1200 0 L1200 570 Q600 530 0 570 Z" fill="#f2f2f2"/>
</svg>
<h2 class="abs serif" style="left:153px;top:1530px;font-size:29px;font-weight:400">About Us</h2>
<div class="rule" style="left:153px;top:1578px"></div>
<h3 class="abs serif" style="left:148px;top:1625px;width:430px;font-size:19px;font-weight:400;line-height:30px">Our 30th year in the kitchen and bath industry!</h3>
<p class="about-text">In 1989, Dan and Mara Whitlock started Harborline Kitchens out of a small storefront in Ashby, MA. In order to find more room for their growing business, they moved their showroom to its current location in Westbrook, MA. 30 years and thousands of happy clients later, Harborline Kitchen and Bath is still committed to exceptional quality of work and design. In early 2019, Sam Keller was brought on to continue the rich tradition of Harborline and work along Dan Whitlock. Both are looking forward to the next chapter in Harborline!</p>
<div class="btn btn-dark" style="left:148px;top:1900px;width:111px;height:35px">Read More</div>
<div class="about-photo"><div class="fill" role="img" aria-label="Photo of an open kitchen leading to a dining room with a blue wall and pendant lights"></div></div>

<!-- PROJECTS -->
<h2 class="section-title" style="top:2075px">Recently Projects</h2>
<div class="rule" style="left:574px;top:2122px"></div>
<div class="project" style="left:0;background:linear-gradient(160deg,#e8e6e2,#9ea5ab 55%,#2f4f8a)" role="img" aria-label="Project photo of a kitchen with a living area and blue rug"></div>
<div class="project" style="left:300px;background:linear-gradient(160deg,#3a3835,#6b655d 50%,#d7d3cc)" role="img" aria-label="Project photo of a dark kitchen with white cabinets and a pendant"></div>
<div class="project" style="left:600px;background:linear-gradient(160deg,#eae6de,#8b7a68 55%,#3c3028)" role="img" aria-label="Project photo of a kitchen with a grey island and wood floor"></div>
<div class="project" style="left:900px;background:linear-gradient(160deg,#d9dde2,#9aa3ab 50%,#384e78)" role="img" aria-label="Project photo of a white kitchen with a dark island"></div>
<div class="btn btn-dark" style="left:545px;top:2505px;width:110px;height:34px">View More</div>

<!-- CTA BAND -->
<div class="cta-photo" role="img" aria-label="Photo of a kitchen with cream cabinets, a window and tile backsplash"></div>
<svg class="abs" style="left:0;top:2598px" width="1200" height="40" viewBox="0 0 1200 40">
  <path d="M0 40 L0 30 Q600 -18 1200 30 L1200 40 Z" fill="#111111"/>
  <path d="M0 0 L1200 0 L1200 20 Q600 -26 0 20 Z" fill="#ffffff"/>
</svg>
<svg class="abs" style="left:0;top:3006px" width="1200" height="44" viewBox="0 0 1200 44">
  <path d="M0 20 Q600 -14 1200 20 L1200 44 L0 44 Z" fill="#ffffff"/>
  <path d="M0 20 Q600 -14 1200 20 L1200 10 Q600 -26 0 10 Z" fill="#111111"/>
</svg>
<div class="abs serif" style="left:0;top:2728px;width:1200px;text-align:center;color:#fff;font-size:19px">Let us create the</div>
<div class="abs serif" style="left:0;top:2762px;width:1200px;text-align:center;color:#fff;font-size:60px;line-height:1">Perfect</div>
<div class="abs serif" style="left:0;top:2840px;width:1200px;text-align:center;color:#fff;font-size:20px">Kitchen or bathroom for you</div>
<div class="btn btn-light" style="left:458px;top:2893px;width:287px;height:36px">Schedule Your Design Consultation Today</div>

<!-- TESTIMONIALS -->
<h2 class="section-title" style="top:3138px">Our Clients Say's</h2>
<div class="rule" style="left:574px;top:3185px"></div>

<div class="quote-side" style="left:-10px;text-align:left">home remodeling of my wife's kitchen and redid my bathroom as well. Every professional came on time and did an amazing job, from the vanity and countertop to the tile, the crew kept the whole remodeling process calm. If you want quality at a fair price, call them and you will not be disappointed.</div>
<div class="qmark" style="left:212px;top:3440px;color:var(--faint)">&#8221;</div>
<div class="abs serif" style="left:0;top:3490px;font-size:15px;color:var(--faint)">R. Prichett</div>

<div class="quote-side" style="left:950px;text-align:center">I recently had the pleasure of working with them on my kitchen and dining room renovation, from design to completion. They are professional, talented, and always responsive to any issue that came up. My kitchen and dining room look beautiful.</div>
<div class="qmark" style="left:918px;top:3286px;color:var(--faint)">&#8220;</div>
<div class="abs serif" style="left:1168px;top:3468px;font-size:15px;color:var(--faint)">Sue Marlowe</div>

<div class="quote-card">
  <p>Harborline Kitchens is the BEST!!! I have worked with Dan on several projects and his expert advice, dedication, and professionalism never ceases to amaze me. This is the place to go!</p>
  <div class="who">Marcus Delaney</div>
</div>
<div class="qmark" style="left:340px;top:3276px">&#8220;</div>
<div class="qmark" style="left:803px;top:3330px">&#8221;</div>
<div class="arrow" style="left:302px;top:3327px"><svg width="12" height="12" viewBox="0 0 12 12"><path d="M8 1 L3 6 L8 11" fill="none" stroke="#111" stroke-width="1.5"/></svg></div>
<div class="arrow" style="left:851px;top:3327px"><svg width="12" height="12" viewBox="0 0 12 12"><path d="M4 1 L9 6 L4 11" fill="none" stroke="#111" stroke-width="1.5"/></svg></div>

<!-- CONTACT -->
<div class="contact-bg" role="img" aria-label="Faded photo of a kitchen counter and backsplash"></div>
<h2 class="section-title" style="top:3659px">Contact Us</h2>
<div class="rule" style="left:574px;top:3706px"></div>
<div class="field" style="left:319px;top:3761px;width:274px;height:33px">Full Name</div>
<div class="field" style="left:604px;top:3761px;width:274px;height:33px">Phone#</div>
<div class="field" style="left:319px;top:3809px;width:559px;height:33px">Email</div>
<div class="field" style="left:319px;top:3855px;width:559px;height:126px">Message</div>
<div class="btn btn-dark" style="left:544px;top:4006px;width:110px;height:34px;font-weight:400">Submit Now</div>

<!-- FOOTER -->
<div class="footer"></div>
<svg class="abs" style="left:0;top:4058px" width="1200" height="40" viewBox="0 0 1200 40">
  <path d="M0 0 L1200 0 L1200 24 Q600 -6 0 24 Z" fill="#ffffff"/>
  <path d="M0 24 Q600 -6 1200 24 L1200 14 Q600 -18 0 14 Z" fill="#111111"/>
  <path d="M0 24 Q600 -6 1200 24 L1200 40 L0 40 Z" fill="#1c1c1c"/>
</svg>
<div class="brand" style="left:75px;top:4180px;color:var(--paper)">
  <span class="brand-mark"></span>
  <span class="brand-name">Harborline<small>Kitchen and Bath, Inc</small></span>
</div>
<p class="foot-text" style="left:75px;top:4252px;width:250px">In 1989, Dan and Mara Whitlock started Harborline Kitchens out of a small storefront in Ashby, MA. In order to find more room for their growing business, they moved their showroom to its current location in Westbrook, MA.</p>
<div class="foot-text" style="left:75px;top:4382px;text-decoration:underline">Read More</div>

<h4 class="foot-head" style="left:407px;font-weight:400">Quick Links</h4>
<ul class="foot-text foot-links" style="left:407px;top:4252px"><li>Home</li><li>About us</li><li>Services</li><li>Projects</li><li>Testimonials</li><li>Contact us</li></ul>

<h4 class="foot-head" style="left:632px;font-weight:400">Contact Us</h4>
<div class="contact-row" style="top:4252px">
  <svg width="12" height="16" viewBox="0 0 12 16"><path d="M6 0 A6 6 0 0 1 12 6 C12 10 6 16 6 16 C6 16 0 10 0 6 A6 6 0 0 1 6 0 Z" fill="#fff"/><circle cx="6" cy="6" r="2.2" fill="#1c1c1c"/></svg>
  <span>48 Orchard Lane<br>Westbrook, MA</span>
</div>
<div class="contact-row" style="top:4310px">
  <svg width="13" height="14" viewBox="0 0 13 14"><path d="M2 0 L5 0 L6 4 L4 5.5 C5 8 6 9 8.5 10 L10 8 L13 9 L13 12 C13 13 12 14 11 14 C5 13 0 8 0 2 C0 1 1 0 2 0 Z" fill="#fff"/></svg>
  <span>555-014-2200</span>
</div>
<div class="contact-row" style="top:4342px">
  <svg width="14" height="12" viewBox="0 0 14 12"><rect x="0.5" y="1.5" width="13" height="9" fill="none" stroke="#fff"/><path d="M0.5 1.5 L7 7 L13.5 1.5" fill="none" stroke="#fff"/></svg>
  <span>sam@harborlinekb.com</span>
</div>

<h4 class="foot-head" style="left:899px;font-weight:400">Our Location</h4>
<div class="abs" style="left:899px;top:4252px;width:226px;height:113px;background:linear-gradient(135deg,#e6eadf,#d4dfe6 50%,#b9cbe0)" role="img" aria-label="Map showing the showroom location"></div>

<div class="bottom-bar"></div>
<div class="foot-text" style="left:75px;top:4502px">Copyright &copy; 2020 harborlinekb.com.All Rights Reserved</div>
<span class="social" style="left:970px"></span>
<span class="social" style="left:1003px"></span>
<span class="social" style="left:1036px"></span>
<span class="social" style="left:1069px"></span>
<span class="social" style="left:1102px"></span>

</body>
</html>
```